Tarquell LLC, needs a web page no more than 5 pages (for now)

Tarquell is a general contractor. Our services include general contracting, design-build construction, disaster recovery and environmental remediation. Our main clients are KRT, QJ, State and Local Gov't Agencies, Hospitals and Schools. Tarquell is also a SDVOSB.

```html
<!DOCTYPE html>
<html lang="en">
<head>
<meta charset="utf-8">
<title>Tarquell – SDVOSB</title>
<link rel="stylesheet" href="https://fonts.googleapis.com/css2?family=Montserrat:wght@600;700&family=Open+Sans:wght@400;600;700&display=swap">
<style>
  :root {
    --ink: #1e2a3a;
    --text: #3a4352;
    --page: #f3f7fb;
    --card: #eff3f8;
    --border: #a9b4c6;
    --gold: #d4a032;
    --footer: #1e2a3a;
    --footer-text: #b9c2cf;
  }
  * { box-sizing: border-box; margin: 0; padding: 0; }
  html, body { width: 862px; height: 1200px; overflow: hidden; }
  body {
    position: relative;
    background: var(--page);
    color: var(--text);
    font-family: "Open Sans", sans-serif;
  }
  .site-header { position: absolute; top: 0; left: 72px; right: 72px; height: 56px; }
  .brand { position: absolute; left: 0; top: 18px; font-family: "Open Sans", sans-serif; font-weight: 700; font-size: 14px; color: var(--ink); }
  .main-nav { position: absolute; right: 0; top: 9px; display: flex; align-items: center; gap: 19px; font-size: 10px; }
  .main-nav a { color: var(--text); text-decoration: none; }
  .main-nav .nav-cta { background: var(--gold); color: var(--ink); width: 65px; height: 25px; display: flex; align-items: flex-end; justify-content: center; padding-bottom: 2px; }
  h1, h2, h3 { font-family: "Montserrat", sans-serif; font-weight: 700; color: var(--ink); }
  .page-title { position: absolute; left: 72px; top: 96px; font-size: 37px; line-height: 47px; letter-spacing: 0.2px; word-spacing: 4px; }
  .intro { position: absolute; left: 72px; top: 189px; width: 720px; font-size: 10.6px; line-height: 17.4px; }
  .card { position: absolute; top: 229px; width: 349px; height: 569px; border: 1px solid var(--border); background: var(--card); padding: 14px; }
  .card-left { left: 72px; }
  .card-right { left: 441px; }
  .card-media { width: 319px; height: 239px; }
  .card h3 { font-size: 19px; }
  .card-left h3 { margin-top: 44px; }
  .card-right h3 { margin-top: 28px; }
  .card p { font-size: 10.8px; line-height: 17.4px; }
  .card-left p:first-of-type { margin-top: 36px; }
  .card-left p + p { margin-top: 37px; }
  .card-right p:first-of-type { margin-top: 17px; }
  .card-right p + p { margin-top: 21px; }
  .facts { list-style: none; margin: 20px 0 0 18px; font-size: 9.5px; line-height: 15.5px; }
  .facts li::before, .benefits li::before { content: "•"; font-size: 7px; vertical-align: top; margin-right: 4px; }
  .facts strong, .benefits strong { color: var(--ink); font-weight: 700; }
  .section-title { position: absolute; left: 72px; top: 866px; font-size: 28px; word-spacing: 3px; }
  .section-lead { position: absolute; left: 72px; top: 906px; width: 720px; font-size: 10.6px; line-height: 17.4px; }
  .benefits { position: absolute; left: 90px; top: 949px; list-style: none; font-size: 9.5px; line-height: 15.5px; }
  .cta { position: absolute; left: 72px; top: 1033px; width: 158px; height: 32px; background: var(--gold); color: var(--ink); font-family: "Montserrat", sans-serif; font-weight: 700; font-size: 9.5px; display: flex; align-items: flex-end; padding: 0 0 6px 16px; text-decoration: none; letter-spacing: 0.3px; }
  .site-footer { position: absolute; left: 0; top: 1122px; width: 862px; height: 78px; background: var(--footer); color: var(--footer-text); }
  .copyright { position: absolute; left: 72px; top: 43px; font-size: 10.6px; }
  .footer-nav { position: absolute; right: 72px; top: 44px; display: flex; gap: 14px; font-size: 8.6px; }
  .footer-nav a { color: var(--footer-text); text-decoration: none; }
</style>
</head>
<body>
  <header class="site-header">
    <div class="brand">Tarquell</div>
    <nav class="main-nav">
      <a href="#">Home</a><a href="#">Services</a><a href="#">Projects</a><a href="#">About Us</a><a href="#">SDVOSB</a>
      <a href="#" class="nav-cta">Contact</a>
    </nav>
  </header>

  <h1 class="page-title">Service-Disabled Veteran-Owned<br>Small Business (SDVOSB)</h1>
  <p class="intro">Tarquell is proud to be a certified Service-Disabled Veteran-Owned Small Business (SDVOSB). Our commitment to excellence, integrity, and discipline stems directly from our military heritage, enabling us to deliver superior results on critical projects.</p>

  <article class="card card-left">
    <svg class="card-media" role="img" aria-label="Photo of a golden wheat field under a cloudy sky" viewBox="0 0 319 239">
      <defs><linearGradient id="fieldTone" x1="0" y1="0" x2="0" y2="1">
        <stop offset="0" stop-color="#d9dcd8"/><stop offset="0.4" stop-color="#c4c6bc"/>
        <stop offset="0.42" stop-color="#b9a85a"/><stop offset="0.7" stop-color="#8a7333"/><stop offset="1" stop-color="#4a3a1c"/>
      </linearGradient></defs>
      <rect width="319" height="239" fill="url(#fieldTone)"/>
    </svg>
    <h3>Our Commitment</h3>
    <p>As an SDVOSB, Tarquell embodies the core values of service, sacrifice, and an unwavering dedication to mission success. We bring these principles to every construction and remediation project, ensuring meticulous planning, robust execution, and ethical stewardship.</p>
    <p>Our veteran leadership team understands the demanding environments of government and institutional contracts, providing unparalleled expertise and a proven track record of reliability.</p>
  </article>

  <article class="card card-right">
    <svg class="card-media" role="img" aria-label="Photo of a whitewashed seaside building with a round tower" viewBox="0 0 319 239">
      <defs><linearGradient id="coastTone" x1="0" y1="0" x2="0" y2="1">
        <stop offset="0" stop-color="#9fb6d6"/><stop offset="0.5" stop-color="#d6dde6"/>
        <stop offset="0.65" stop-color="#e8d5a8"/><stop offset="1" stop-color="#c9ad7a"/>
      </linearGradient></defs>
      <rect width="319" height="239" fill="url(#coastTone)"/>
    </svg>
    <h3>SDVOSB Certification Details</h3>
    <p>Tarquell holds current and verified SDVOSB certification through the Office of Veteran Credentials (QJ) as part of the Vets Forward program, ensuring our eligibility for set-aside contracts and sole-source opportunities within the federal marketplace.</p>
    <p>Our DUNS number and CAGE code are available upon request for verification purposes, affirming our status as a trusted federal contractor.</p>
    <ul class="facts">
      <li><strong>Certifying Body:</strong> Office of Veteran Credentials (QJ)</li>
      <li><strong>Program:</strong> Vets Forward</li>
      <li><strong>Status:</strong> Verified &amp; Active</li>
    </ul>
  </article>

  <h2 class="section-title">Advantages of Partnering with an SDVOSB</h2>
  <p class="section-lead">Choosing Tarquell for your projects offers distinct benefits, particularly for federal agencies and prime contractors seeking to meet their small business contracting goals:</p>
  <ul class="benefits">
    <li><strong>Federal Set-Aside Contracts:</strong> The QJ has exclusive authority to set aside contracts for SDVOSBs, providing direct access to a qualified pool of contractors.</li>
    <li><strong>Sole-Source Opportunities:</strong> Contracts under a certain threshold can be awarded non-competitively to qualified SDVOSBs.</li>
    <li><strong>Subcontracting Goals:</strong> Prime contractors can fulfill their subcontracting requirements by partnering with Tarquell.</li>
    <li><strong>Proven Performance:</strong> SDVOSBs are known for their strong work ethic, integrity, and commitment to delivering high-quality results.</li>
    <li><strong>Tax Incentives:</strong> Some states and local governments offer tax incentives for working with veteran-owned businesses.</li>
  </ul>
  <a href="#" class="cta">View Our Federal Projects</a>

  <footer class="site-footer">
    <p class="copyright">© 2024 Tarquell. All Rights Reserved.</p>
    <nav class="footer-nav"><a href="#">Privacy Policy</a><a href="#">Terms of Service</a><a href="#">Sitemap</a></nav>
  </footer>
</body>
</html>
```